Refresh Home Page for Photography Training Site

http://brannockcourses.example/

My site is looking kind of out-of-date, so it's time for a face lift. I want to bring it up to date with a more modern web look.

What I need from you is a home page design concept. No coding, just a PSD design, but it MUST be something that a coder could build into an efficient, fast-loading page. After the home page design contest is finished, we can work together privately, if you want to continue, to design the rest of the pages in the site for additional fees.

Functionally, the new page needs to do the same job as the current home page, just do it more efficiently (if possible) while looking fresh and modern.

Sites I like
http://vantri.example/ (clean, modern)

Competitor sites:
http://dorwinlessons.example/
http://www.glenmarshallphotography.example/

Target Market(s)

Amateur and semi-professional photographers

Industry/Entity Type

Training

Requirements
Must have
• MUST HAVE
1. A prominent space where testimonials appear in rotation, one after another (instead of the one large testimonial on the current site).

2. My photo in the header. It can be smaller than at present. If you prefer you can use the black and white photo from the about page. Put a signature saying Ron Brannock near the photo, in a better handwritten style than the current signature, which is a lame font.

3. Tagline "Learn Photography and Image Editing the Easy Way"
Should not have
• No flash or other fancy technology. (However it is acceptable to design an area that would be an image carousel, where one image changes to another, then another, etc. Like the Glen Marshall or Vantri site. That is not too fancy, but it's optional).

```html
<!DOCTYPE html>
<html lang="en">
<head>
<meta charset="utf-8">
<title>Brannock Training – Learn Photography and Image Editing the Easy Way</title>
<link rel="stylesheet" href="https://fonts.googleapis.com/css2?family=Arimo:wght@400;700&family=Open+Sans:wght@300;400&family=Parisienne&display=swap">
<style>
:root{
  --page:#ffffff;
  --panel:#2f2f30;
  --card:#ffffff;
  --rule:#e3e3e3;
  --accent:#4d8fae;
  --accent-soft:#6aa9c7;
  --ribbon:#3f93bf;
  --ribbon-dark:#2a6c8f;
  --ink:#333333;
  --body:#444444;
  --muted:#999999;
}
*{box-sizing:border-box;margin:0;padding:0}
html,body{width:947px;height:1200px;overflow:hidden;background:var(--page)}
body{position:relative;font-family:"Arimo",Arial,sans-serif;color:var(--body)}
.abs{position:absolute}
.stage{left:14px;top:13px;width:922px;height:1187px;
  background:var(--panel);
  background-image:repeating-linear-gradient(45deg,rgba(255,255,255,.018) 0 2px,transparent 2px 5px)}

/* header */
.portrait{left:84px;top:20px;width:137px;height:133px;border-radius:60px 60px 0 0;
  background:linear-gradient(180deg,#6a5a48 0%,#c9a07e 35%,#b88a63 58%,#8fc2e6 62%,#79b3de 100%)}
.signature{left:200px;top:90px;font-family:"Parisienne",cursive;font-size:28px;color:#d8d8d8;white-space:nowrap}
.brand{left:380px;top:101px;font-family:"Open Sans",sans-serif;font-weight:300;font-size:18px;letter-spacing:.5px;color:#e4e4e4}
.tagline{left:381px;top:124px;font-family:"Open Sans",sans-serif;font-size:8.5px;letter-spacing:.3px;color:#bdbdbd;text-transform:uppercase}
.nav{left:360px;top:41px;width:506px;height:40px;background:var(--card);border-radius:3px;display:flex;box-shadow:0 2px 3px rgba(0,0,0,.35)}
.nav a{flex:auto;display:flex;align-items:center;justify-content:center;font-size:13px;font-weight:700;color:var(--accent);text-decoration:none;border-right:1px solid var(--rule)}
.nav a:last-child{border-right:0}
.share{top:94px;height:18px;display:flex;align-items:center;gap:4px;font-size:10px;font-weight:700}
.share .btn{height:18px;padding:0 5px 0 4px;display:flex;align-items:center;gap:3px;background:#f2f2f2;border:1px solid #c9c9c9;border-radius:2px;color:#4a5f7e}
.share .btn i{width:9px;height:9px;background:#7f94b4;display:block}
.share .count{height:18px;padding:0 4px;display:flex;align-items:center;background:#fff;border:1px solid #c9c9c9;border-radius:2px;color:#333}

/* hero */
.hero{left:82px;top:153px;width:785px;height:392px;background:var(--card);box-shadow:0 2px 6px rgba(0,0,0,.4)}
.hero-frame{left:20px;top:20px;width:745px;height:352px;border:1px solid #d9d9d9;
  background:linear-gradient(90deg,#e9e9ec 0%,#f4f3f6 45%,#f2eff1 100%)}
.hero-photo{right:0;top:0;width:344px;height:350px;background:linear-gradient(90deg,#f0ecef 0%,#d9b596 30%,#b07a4f 65%,#8a5a36 100%)}
.hero h1{left:28px;top:84px;width:440px;font-size:24.5px;line-height:32px;font-weight:400;color:var(--ink);letter-spacing:-.2px}
.hero p{left:32px;top:160px;width:370px;font-size:13.5px;line-height:20px;color:var(--ink)}
.hero .cta{left:32px;top:247px;width:107px;height:33px;border-radius:17px;background:linear-gradient(#8a8a8a,#555);box-shadow:0 0 0 3px #cfcfcf,inset 0 1px 0 rgba(255,255,255,.3);color:#fff;font-size:12px;display:flex;align-items:center;justify-content:center}
.ribbon{left:-18px;top:-6px;width:140px;height:140px}
.ribbon-text{font-family:"Arimo",sans-serif;font-weight:700;font-size:15px;fill:#fff}
.slide-arrow{top:324px;width:50px;height:50px;border-radius:50%;background:#444;display:flex;align-items:center;justify-content:center}

/* cards */
.card{background:var(--card);border-radius:2px;box-shadow:0 2px 5px rgba(0,0,0,.45)}
.card h2{position:absolute;font-size:20.5px;font-weight:400;color:var(--accent)}
.courses{left:70px;top:577px;width:520px;height:533px}
.courses h2{left:17px;top:18px}
.courses .rule{left:10px;height:1px;width:500px;background:var(--rule)}
.thumb{border:5px solid #e4e4e4;box-shadow:0 0 0 1px #d0d0d0}
.course-thumb{left:19px;width:143px;height:106px}
.course-title{left:184px;width:280px;font-size:13px;line-height:17px;font-weight:700;color:var(--accent)}
.course-desc{left:184px;width:326px;font-size:11px;line-height:17.5px;color:var(--ink)}
.course-desc .new{color:var(--accent-soft);font-weight:700}
.course-meta{left:184px;font-family:Georgia,serif;font-style:italic;font-size:10px;color:var(--muted)}
.more{display:flex;align-items:center;gap:8px;font-size:11.5px;font-weight:700;color:var(--accent)}
.see-all{display:flex;align-items:center;gap:9px;font-size:11.5px;font-weight:700;color:var(--accent)}
.see-all .dot{width:25px;height:25px;border-radius:50%;background:linear-gradient(#8fc6e2,#4a9ac3);display:flex;align-items:center;justify-content:center;box-shadow:0 0 0 2px #dceef7}

.tutorials{left:611px;top:577px;width:275px;height:346px}
.tutorials h2{left:20px;top:18px}
.tut-thumb{left:20px;width:87px;height:64px;border-width:3px}
.tut-title{left:119px;width:125px;font-size:12.5px;line-height:16px;font-weight:700;color:var(--accent)}
.tutorials .rule{left:18px;width:240px;height:1px;background:var(--rule)}
.free{right:-12px;top:-4px;width:100px;height:100px}

.testimonials{left:611px;top:937px;width:275px;height:173px}
.testimonials h2{left:17px;top:17px}
.quote{left:41px;top:56px;width:212px;font-size:14px;line-height:19px;color:var(--accent-soft)}
.quote .who{font-size:11px;color:var(--muted)}
.quote .who b{color:#888}
.qmark{font-family:Georgia,serif;font-weight:700;font-size:28px;color:#b5b5b5}

.footer{right:76px;top:1155px;font-size:9.5px;color:#a8a8a8;display:flex;gap:7px}
</style>
</head>
<body>
<div class="abs stage"></div>

<header>
  <div class="abs portrait" role="img" aria-label="Portrait photo of Ron Brannock in a light blue shirt"></div>
  <div class="abs signature">Ron Brannock</div>
  <div class="abs brand">BRANNOCK TRAINING</div>
  <div class="abs tagline">Learning photography and image editing the easy way</div>
  <nav class="abs nav">
    <a>Home</a><a>About</a><a>Courses</a><a>Free Tutorials</a><a>FAQs</a><a>Contact</a>
  </nav>
  <div class="abs share" style="left:626px"><span class="btn"><i></i>Like</span><span class="count">817</span></div>
  <div class="abs share" style="left:709px"><span class="btn"><i></i>Share</span><span class="count">66</span></div>
  <div class="abs share" style="left:810px"><span class="btn"><i></i>Vote</span><span class="count">3</span></div>
</header>

<section class="abs hero">
  <div class="abs hero-frame">
    <div class="abs hero-photo" role="img" aria-label="Beauty portrait of a woman with long auburn hair"></div>
    <h1 class="abs">Start learning today how to take your own professional looking photographs</h1>
    <p class="abs">From ameteur to professional theres a course, or tutorial to teach you different pro techniques for taking the perfect photo, step by step</p>
    <div class="abs cta">Find out more</div>
  </div>
  <svg class="abs ribbon" viewBox="0 0 140 140">
    <polygon points="0,66 0,104 104,0 66,0" fill="var(--ribbon)"/>
    <polygon points="0,104 12,104 0,116" fill="var(--ribbon-dark)"/>
    <text class="ribbon-text" transform="translate(22,70) rotate(-45)">START NOW!</text>
  </svg>
</section>
<div class="abs slide-arrow" style="left:53px"><svg width="14" height="16" viewBox="0 0 14 16"><path d="M10 2 4 8l6 6" stroke="#fff" stroke-width="3" fill="none"/></svg></div>
<div class="abs slide-arrow" style="left:853px"><svg width="14" height="16" viewBox="0 0 14 16"><path d="M4 2l6 6-6 6" stroke="#fff" stroke-width="3" fill="none"/></svg></div>

<section class="abs card courses">
  <h2>Latest Online Training Courses</h2>
  <div class="abs rule" style="top:53px"></div>

  <div class="abs thumb course-thumb" style="top:71px;background:linear-gradient(90deg,#2b3c52 0 40%,#f3f3f3 40%)" role="img" aria-label="Image editing software box beside a model portrait"></div>
  <div class="abs course-title" style="top:78px">Pixelshop basics for photographers</div>
  <div class="abs course-desc" style="top:101px"><span class="new">NEW!</span> Learn the core Pixelshop skills every photographer needs in this easy, 10-lesson video course.</div>
  <div class="abs course-meta" style="top:170px">9 (series) videos &nbsp;|&nbsp; 3 hours</div>
  <div class="abs more" style="left:390px;top:167px"><svg width="8" height="12" viewBox="0 0 8 12"><path d="M1 1l5 5-5 5" stroke="var(--accent)" stroke-width="2.5" fill="none"/></svg>Find out more</div>
  <div class="abs rule" style="top:197px"></div>

  <div class="abs thumb course-thumb" style="top:212px;background:linear-gradient(90deg,#8a6a52,#3a7a5a 50%,#c9c9c9)" role="img" aria-label="Collage of headshot photos with a flash unit"></div>
  <div class="abs course-title" style="top:213px">How to shoot professional headshots on a budget with a small flash</div>
  <div class="abs course-desc" style="top:250px">This 9-video course, will teach you all you need to know about off-camera lighting with your digital SLR's detachable flash!</div>
  <div class="abs course-meta" style="top:313px">13 (series) videos &nbsp;|&nbsp; 2.5 hours</div>
  <div class="abs more" style="left:390px;top:310px"><svg width="8" height="12" viewBox="0 0 8 12"><path d="M1 1l5 5-5 5" stroke="var(--accent)" stroke-width="2.5" fill="none"/></svg>Find out more</div>
  <div class="abs rule" style="top:340px"></div>

  <div class="abs thumb course-thumb" style="top:355px;background:linear-gradient(90deg,#1a1a1a 0 55%,#f2f2f2 55%)" role="img" aria-label="Photo software box and a DSLR camera"></div>
  <div class="abs course-title" style="top:357px">Lumaroom basics for photographers</div>
  <div class="abs course-desc" style="top:380px">Learn how Lumaroom can help you take your photography to the next level in this introductory video course.</div>
  <div class="abs course-meta" style="top:454px">1 videos &nbsp;|&nbsp; - hours</div>
  <div class="abs more" style="left:390px;top:451px"><svg width="8" height="12" viewBox="0 0 8 12"><path d="M1 1l5 5-5 5" stroke="var(--accent)" stroke-width="2.5" fill="none"/></svg>Find out more</div>
  <div class="abs rule" style="top:485px"></div>

  <div class="abs see-all" style="left:22px;top:498px"><span class="dot"><svg width="8" height="11" viewBox="0 0 8 11"><path d="M1 1l5 4.5-5 4.5" stroke="#fff" stroke-width="2.5" fill="none"/></svg></span>See all courses available</div>
</section>

<section class="abs card tutorials">
  <h2>Online Tutorials</h2>
  <div class="abs thumb tut-thumb" style="top:58px;background:linear-gradient(135deg,#2a1a0e,#b07a3e 55%,#3a2612)" role="img" aria-label="Chess pieces with shallow depth of field"></div>
  <div class="abs tut-title" style="top:59px">Understanding Depth of field</div>
  <div class="abs more" style="left:119px;top:106px"><svg width="8" height="12" viewBox="0 0 8 12"><path d="M1 1l5 5-5 5" stroke="var(--accent)" stroke-width="2.5" fill="none"/></svg>Find out more</div>
  <div class="abs rule" style="top:135px"></div>

  <div class="abs thumb tut-thumb" style="top:146px;background:linear-gradient(135deg,#7a6a58,#d8c8b2 55%,#5a4a3a)" role="img" aria-label="Video still of a model shoot in a hotel room"></div>
  <div class="abs tut-title" style="top:147px">Model Shot at Stone Harbor Hotel</div>
  <div class="abs more" style="left:119px;top:194px"><svg width="8" height="12" viewBox="0 0 8 12"><path d="M1 1l5 5-5 5" stroke="var(--accent)" stroke-width="2.5" fill="none"/></svg>Find out more</div>
  <div class="abs rule" style="top:223px"></div>

  <div class="abs thumb tut-thumb" style="top:233px;background:linear-gradient(135deg,#2a2a2a,#8a7a70 55%,#e8e8e8)" role="img" aria-label="Woman holding a camera with flash"></div>
  <div class="abs tut-title" style="top:235px">Flash Photography tips (video)</div>
  <div class="abs more" style="left:119px;top:282px"><svg width="8" height="12" viewBox="0 0 8 12"><path d="M1 1l5 5-5 5" stroke="var(--accent)" stroke-width="2.5" fill="none"/></svg>Find out more</div>

  <div class="abs see-all" style="left:19px;top:313px"><span class="dot"><svg width="8" height="11" viewBox="0 0 8 11"><path d="M1 1l5 4.5-5 4.5" stroke="#fff" stroke-width="2.5" fill="none"/></svg></span>See all free available tutorials</div>

  <svg class="abs free" viewBox="0 0 100 100">
    <polygon points="14,0 52,0 100,48 100,86" fill="var(--ribbon)"/>
    <polygon points="100,86 100,98 88,86" fill="var(--ribbon-dark)"/>
    <text class="ribbon-text" transform="translate(44,16) rotate(45)">FREE!</text>
  </svg>
</section>

<section class="abs card testimonials">
  <h2>Testimonals</h2>
  <div class="abs qmark" style="left:17px;top:46px">&ldquo;</div>
  <p class="abs quote">I love your videos! I can learn more in one hour than in a month of studying photography books! <span class="who"><b>Dale R</b> &nbsp;|&nbsp; Dayton OH</span></p>
  <div class="abs qmark" style="left:241px;top:106px">&rdquo;</div>
  <div class="abs see-all" style="left:19px;top:139px"><span class="dot"><svg width="8" height="11" viewBox="0 0 8 11"><path d="M1 1l5 4.5-5 4.5" stroke="#fff" stroke-width="2.5" fill="none"/></svg></span>See all testimonials</div>
</section>

<footer class="abs footer"><span>Terms &amp; Conditions</span><span>|</span><span>Privacy</span><span style="margin-left:14px">© 2011 Ron Brannock</span></footer>
</body>
</html>
```